Tui Netlink Website

We're looking for a basic website and order form for our stripped down ISP, Tui Netlink.

The front page should be basic with our two plan options - we're open to pretty much any design, but one possibility is an image of New Zealand with two clouds above it (similar to the quick mockup attached).

Clicking on one of the plans will then take the user to a basic order form.

We will also need a contact, about, and support page.

Industry/Entity Type

Isp

```html
<!DOCTYPE html>
<html lang="en">
<head>
<meta charset="utf-8">
<title>Tui Netlink — Pure Broadband</title>
<link rel="stylesheet" href="https://fonts.googleapis.com/css2?family=Montserrat:wght@500;600;700;800&family=Open+Sans:wght@400;600;700&family=Questrial&display=swap">
<style>
:root{
  --purple:#6a3a9c;
  --purple-deep:#4e2680;
  --purple-glass:rgba(110,60,170,.55);
  --purple-band:rgba(120,70,180,.72);
  --ink:#1c1c1c;
  --outline:#2a2233;
  --white:#ffffff;
  --paper:#f4f2f6;
  --price:#8a58c2;
}
*{box-sizing:border-box;margin:0;padding:0}
html,body{width:968px;height:1200px;overflow:hidden;background:#111}
body{font-family:"Open Sans",Arial,sans-serif;color:var(--white);position:relative}
.section{position:absolute;left:0;width:968px;overflow:hidden}
.photo{position:absolute;inset:0}
.section-title{position:absolute;font-family:"Montserrat",Arial,sans-serif;font-weight:700;font-size:26px;letter-spacing:3px;color:var(--white);text-shadow:0 1px 3px rgba(0,0,0,.5)}
.nav-arrow{position:absolute}

/* hero */
.hero{top:0;height:220px}
.hero .photo{background:linear-gradient(180deg,#3f7fc8 0%,#8fb3de 22%,#8c7fb8 45%,#6a5a8a 60%,#6b6440 70%,#4d4a2e 100%)}
.hero-band{position:absolute;left:0;top:65px;width:968px;height:80px;background:var(--purple-band)}
.brand-name{position:absolute;left:150px;top:34px;width:650px;text-align:center;font-family:"Montserrat",Arial,sans-serif;font-weight:800;font-size:38px;letter-spacing:3px;color:var(--white)}
.tagline{position:absolute;left:474px;top:76px;font-family:"Questrial",Arial,sans-serif;font-size:18px;line-height:20px;color:var(--white)}
.hero-cloud{position:absolute;top:74px;width:155px;height:80px}
.hero-cloud svg{position:absolute;left:0;top:0}
.hero-cloud .price{position:absolute;left:0;width:100%;top:10px;text-align:center;font-family:"Montserrat",Arial,sans-serif;font-weight:700;font-size:17px;line-height:16px;color:var(--white);text-shadow:-1px -1px 0 var(--outline),1px -1px 0 var(--outline),-1px 1px 0 var(--outline),1px 1px 0 var(--outline)}
.hero-cloud .price small{display:block;font-size:10px;line-height:11px;font-weight:600}
.map-area{position:absolute;left:640px;top:50px;width:220px;height:104px;background:radial-gradient(ellipse at center,rgba(255,255,255,.95) 0%,rgba(255,255,255,.85) 45%,rgba(255,255,255,0) 72%)}
.learn-more{position:absolute;left:446px;top:176px;font-size:10px;color:#eee}

/* about */
.about{top:220px;height:252px}
.about .photo{background:linear-gradient(180deg,#c99ac0 0%,#b98aa8 25%,#8f7a8a 45%,#54523f 65%,#3e3a30 100%)}
.about .section-title{left:42px;top:76px}
.about-copy{position:absolute;left:220px;top:45px;width:515px;height:135px;background:var(--purple-glass);padding:4px 20px;font-size:10.3px;line-height:11.5px;color:var(--white)}
.about-copy p{text-indent:2em;margin-bottom:5px}

/* plans */
.plans{top:472px;height:253px}
.plans .photo{background:radial-gradient(ellipse at 50% 100%,#c9d8ff 0%,#3a5ee0 25%,#3a2a9c 55%,#1a1240 80%,#0b0820 100%)}
.plans .section-title{left:42px;top:104px}
.plans-frame{position:absolute;left:272px;top:68px;width:400px;height:162px;background:rgba(255,255,255,.35);border-radius:6px}
.plan-card{position:absolute;top:80px;width:182px;height:142px;border-radius:4px;overflow:hidden;background:var(--paper)}
.plan-card .price{height:32px;text-align:center;font-family:"Questrial",Arial,sans-serif;font-size:22px;line-height:32px;color:var(--price)}
.plan-card .speed,.plan-card .cap{background:var(--ink);text-align:center;font-size:10px;font-weight:600;color:var(--white)}
.plan-card .speed{height:22px;line-height:22px}
.plan-card .cap{height:26px;line-height:22px;font-size:8px;font-weight:700}
.plan-card .name{height:27px;text-align:center;font-family:"Montserrat",Arial,sans-serif;font-weight:800;font-size:20px;line-height:27px;color:#3a2a50;background:linear-gradient(180deg,#fff,#ddd)}
.plan-card .foot{height:35px;background:var(--purple);display:flex;align-items:center;justify-content:center}
.signup{width:116px;height:15px;background:var(--white);border-radius:3px;text-align:center;font-size:9.5px;font-weight:700;line-height:15px;color:var(--purple-deep)}
.plan-cloud{position:absolute;top:10px;width:192px;height:78px}

/* support */
.support{top:725px;height:253px}
.support .photo{background:linear-gradient(180deg,#2c4a7a 0%,#3a5684 18%,#1d2a44 40%,#2e2a30 65%,#5a3a3a 85%,#2a2226 100%)}
.support .section-title{left:42px;top:103px}
.support-panel{position:absolute;left:282px;top:61px;width:476px;height:157px;background:rgba(120,60,180,.6)}
.support-tab{position:absolute;top:-3px;font-size:7px;font-weight:700;color:var(--white)}
.faq-btn{position:absolute;left:15px;width:168px;height:26px;background:var(--purple-deep);border-radius:5px;padding-left:21px;font-size:9px;font-weight:700;line-height:26px;color:var(--white)}
.answer{position:absolute;left:188px;top:16px;width:275px;height:86px;background:rgba(255,255,255,.22);padding:8px 28px}
.answer h3{font-family:"Questrial",Arial,sans-serif;font-weight:400;font-size:20px;line-height:20px;margin-bottom:4px}
.answer p{font-size:8.5px;line-height:9px}

/* contact */
.contact{top:978px;height:222px}
.contact .photo{background:linear-gradient(180deg,#1f3a3c 0%,#2c4446 30%,#3e4438 50%,#2a2a20 70%,#4a3a24 88%,#1c1a16 100%)}
.contact .section-title{left:50px;top:48px;font-size:25px;letter-spacing:1px}
.field{position:absolute;left:506px;width:261px;background:var(--white);font-size:8.5px;color:#666;padding:2px 6px}
.submit-btn{position:absolute;left:508px;top:126px;width:92px;height:12px;background:var(--purple);font-size:9px;line-height:12px;text-align:center;color:var(--white)}
</style>
</head>
<body>

<header class="section hero">
  <div class="photo" role="img" aria-label="Photo of a long straight road running through open grassland toward mountains under a blue sky"></div>
  <div class="hero-band"></div>
  <div class="brand-name">TUI NETLINK.</div>
  <div class="hero-cloud" style="left:113px">
    <svg width="155" height="80" viewBox="0 0 155 80"><path d="M20 58 Q2 58 4 44 Q6 30 24 32 Q28 10 52 14 Q70 2 88 14 Q112 8 118 30 Q148 28 148 46 Q148 60 130 60 Z" fill="#fff"/><path d="M68 52 H88 V62 H98 L78 79 L58 62 H68 Z" fill="#fff" stroke="#333" stroke-width="2"/></svg>
    <div class="price">$95<small>up to 30Mps<br>down</small></div>
  </div>
  <div class="hero-cloud" style="left:270px;top:68px">
    <svg width="155" height="80" viewBox="0 0 155 80"><path d="M20 58 Q2 58 4 44 Q6 30 24 32 Q28 10 52 14 Q70 2 88 14 Q112 8 118 30 Q148 28 148 46 Q148 60 130 60 Z" fill="#fff"/><path d="M68 52 H88 V62 H98 L78 79 L58 62 H68 Z" fill="#fff" stroke="#333" stroke-width="2"/></svg>
    <div class="price">$99<small>up to 100Mps<br>down</small></div>
  </div>
  <div class="tagline">Pure Broadband.<br>Pure Speed.<br>No Limits.</div>
  <div class="map-area" role="img" aria-label="White map silhouette of New Zealand"></div>
  <div class="learn-more">Learn More</div>
</header>

<section class="section about">
  <div class="photo" role="img" aria-label="Photo of a lakeside town at dusk with snow-capped mountains under a pink sky"></div>
  <h2 class="section-title">ABOUT</h2>
  <div class="about-copy">
    <p>Lorem ipsum dolor sit amet, consectetur adipiscing elit. Maecenas vitae interdum metus, eget pharetra leo. Donec eros tortor, eleifend sed molestie a, ultrices vel nibh. Vestibulum blandit, nunc eu adipiscing mattis, dui ante pulvinar diam, quis tristique nibh elit id tortor. Nullam metus dolor, aliquam sed odio quis, scelerisque interdum felis. Ut in fermentum tortor. Morbi et lacinia nunc. Aenean elementum mollis enim bibendum pellentesque.</p>
    <p>Pellentesque habitant morbi tristique senectus et netus et malesuada fames ac turpis egestas. Praesent vulputate orci turpis, eu viverra nibh vehicula in. Phasellus pretium at orci nec suscipit. Sed vel enim tempus, malesuada risus eget, rutrum purus. Praesent in purus dapibus, luctus nibh eu, ultricies arcu. Quisque cursus blandit ante id consequat. Sed vitae arcu ac neque porttitor vehicula quis consectetur est. Morbi vel est eleifend, rutrum magna nec, laoreet justo.</p>
  </div>
  <svg class="nav-arrow" style="left:447px;top:190px" width="40" height="40" viewBox="0 0 40 40"><path d="M12 0 H28 V18 H40 L20 38 L0 18 H12 Z" fill="#6a3a9c" opacity=".85"/></svg>
</section>

<section class="section plans">
  <div class="photo" role="img" aria-label="Abstract photo of blue and violet light streaks converging toward a bright centre"></div>
  <h2 class="section-title">PLANS</h2>
  <div class="plans-frame"></div>
  <svg class="plan-cloud" style="left:280px" viewBox="0 0 192 78"><path d="M22 72 Q2 72 4 54 Q6 38 26 40 Q30 12 62 16 Q84 0 108 14 Q138 8 146 36 Q186 34 188 54 Q190 72 168 72 Z" fill="#fff"/><path d="M82 36 H110 V52 H124 L96 76 L68 52 H82 Z" fill="#fff" stroke="#2a2a3a" stroke-width="2.5"/></svg>
  <svg class="plan-cloud" style="left:476px" viewBox="0 0 192 78"><path d="M22 72 Q2 72 4 54 Q6 38 26 40 Q30 12 62 16 Q84 0 108 14 Q138 8 146 36 Q186 34 188 54 Q190 72 168 72 Z" fill="#fff"/><path d="M82 36 H110 V52 H124 L96 76 L68 52 H82 Z" fill="#fff" stroke="#2a2a3a" stroke-width="2.5"/></svg>
  <article class="plan-card" style="left:283px">
    <div class="price">$95</div>
    <div class="speed">Up to 30Mps down</div>
    <div class="name">Tui One.</div>
    <div class="cap">500GB/month</div>
    <div class="foot"><div class="signup">Signup Now</div></div>
  </article>
  <article class="plan-card" style="left:480px">
    <div class="price">$99</div>
    <div class="speed">Up to 100Mps down</div>
    <div class="name">Tui Two.</div>
    <div class="cap">Unlimited</div>
    <div class="foot"><div class="signup">Signup Now</div></div>
  </article>
  <svg class="nav-arrow" style="left:0;top:208px" width="34" height="45" viewBox="0 0 34 45"><path d="M0 0 L20 20 H10 V45 H0 Z" fill="#6a3a9c" opacity=".85"/></svg>
  <svg class="nav-arrow" style="left:855px;top:208px" width="62" height="42" viewBox="0 0 62 42"><path d="M21 0 H41 V20 H62 L31 42 L0 20 H21 Z" fill="#6a3a9c" opacity=".9"/></svg>
</section>

<section class="section support">
  <div class="photo" role="img" aria-label="Night photo of a city skyline with light trails on a motorway"></div>
  <h2 class="section-title">SUPPORT</h2>
  <div class="support-panel">
    <span class="support-tab" style="left:110px">FAQ</span>
    <span class="support-tab" style="left:322px">SUBMIT TICKET</span>
    <div class="faq-btn" style="top:16px">FAQ TITLE #1</div>
    <div class="faq-btn" style="top:48px">FAQ TITLE #2</div>
    <div class="faq-btn" style="top:80px">FAQ TITLE #3</div>
    <div class="answer">
      <h3>Answer #1</h3>
      <p>Lorem ipsum dolor sit amet, consectetur adipiscing elit. Donec vitae feugiat justo, vel dictum ipsum. Nam varius scelerisque libero, sit amet consequat metus cursus in.</p>
    </div>
  </div>
  <svg class="nav-arrow" style="left:0;top:198px" width="36" height="42" viewBox="0 0 36 42"><path d="M0 0 L22 20 H12 V42 H0 Z" fill="#6a3a9c" opacity=".85"/></svg>
  <svg class="nav-arrow" style="left:855px;top:198px" width="62" height="42" viewBox="0 0 62 42"><path d="M21 0 H41 V20 H62 L31 42 L0 20 H21 Z" fill="#6a3a9c" opacity=".9"/></svg>
</section>

<section class="section contact">
  <div class="photo" role="img" aria-label="Night photo of a lakeside town lit up beneath hills and a starry sky"></div>
  <h2 class="section-title">CONTACT US</h2>
  <div class="field" style="top:33px;height:15px">Enter Name</div>
  <div class="field" style="top:59px;height:15px">Enter Email</div>
  <div class="field" style="top:84px;height:32px">Enter Your Message</div>
  <div class="submit-btn">Submit</div>
  <svg class="nav-arrow" style="left:852px;top:147px" width="64" height="40" viewBox="0 0 64 40"><path d="M32 0 L64 20 H43 V40 H21 V20 H0 Z" fill="#6a3a9c" opacity=".9"/></svg>
</section>

</body>
</html>
```